ARC VOLLEY Business Card Project

I'd like to request a business card design for the new company I've launched.
The name of the company is "ARC VOLLEY" an indoor unmanned tennis practice facility.
We would like to see designs that use our brand identity color in the logo I've attached.
We hope to get the design with modern, luxurious and elegant tone and manner.
We hope the logo should not be too big.

Business card must have elements as below:
- Logo (One of the logos I've attached)
- Name (In Korean Text) : 박 서 윤
- Title (In Korean Text) : 대표
- Phone Number : 010-8472-3916
- Email Address : seoyun.park@arcvolley-example.co.kr
- Website : www.arcvolley-example.co.kr
- Instagram : arcvolley
- Address (In Korean text) : 경기도 용인시 수지구 풍덕천로 456 미래타워 5층 501호, 502호

Target Market(s)

Tennis amateurs in 20 to 40s

Industry/Entity Type

Sports, Hobby

Contact Information for Business Card

- Logo (One of the logos I've attached) - Name (In Korean Text) : 박 서 윤 - Title (In Korean Text) : 대표 - Phone Number : 010-8472-3916 - Email Address : seoyun.park@arcvolley-example.co.kr - Website : www.arcvolley-example.co.kr - Instagram : arcvolley - Address (In Korean text) : 경기도 용인시 수지구 풍덕천로 456 미래타워 5층 501호, 502호

Font styles to use
Sans Serif

Requirements
Must have
• Double sided
Nice to have
• Logo with intaglio or relief embossing
Should not have
• Logo should not be too big.

```html
<!DOCTYPE html>
<html lang="ko">
<head>
<meta charset="utf-8">
<title>ARC VOLLEY Business Card</title>
<link href="https://fonts.googleapis.com/css2?family=Noto+Sans+KR:wght@300;400;500;700&display=swap" rel="stylesheet">
<style>
  :root {
    --backdrop: #9b9b9b;
    --paper: #f6f6f4;
    --brand-green: #1f4a2e;
    --deep-green: #13341f;
    --band-green: #2f5e3f;
    --rule-dark: #4a4a4a;
    --ink-soft: #6a6a6a;
    --paper-text: #eef2ee;
  }
  * { margin: 0; padding: 0; box-sizing: border-box; }
  html, body { width: 1200px; height: 1050px; overflow: hidden; }
  body {
    background: var(--backdrop);
    font-family: "Noto Sans KR", sans-serif;
    display: flex; flex-direction: column; align-items: center; justify-content: center;
    gap: 30px;
  }
  .card {
    position: relative;
    width: 840px; height: 480px;
    box-shadow: 0 10px 30px rgba(0,0,0,.25);
  }
  .card--front { background: var(--paper); }
  .card--back { background: var(--deep-green); }

  .brand-name {
    position: absolute;
    font-weight: 700;
    letter-spacing: 2px;
    font-size: 34px;
  }
  .card--front .brand-name { top: 70px; right: 70px; color: var(--brand-green); }
  .card--back .brand-name { bottom: 130px; right: 70px; color: var(--paper-text); }

  .holder { position: absolute; left: 60px; top: 220px; }
  .holder__name { font-size: 28px; font-weight: 700; color: var(--brand-green); letter-spacing: 2px; }
  .holder__title { font-size: 20px; font-weight: 300; color: var(--ink-soft); margin-top: 2px; }

  .contact {
    position: absolute;
    display: flex; align-items: center; gap: 10px;
    font-size: 17px; font-weight: 300; color: var(--ink-soft);
    white-space: nowrap;
  }
  .contact svg { width: 16px; height: 16px; flex: none; }
  .contact--phone { left: 60px; top: 308px; }
  .contact--phone svg { fill: var(--brand-green); }
  .contact--email { right: 60px; top: 352px; }
  .contact--address { left: 60px; top: 394px; font-size: 14px; }
  .contact--instagram { right: 60px; top: 394px; font-size: 14px; }
  .contact__label { font-weight: 500; color: var(--brand-green); }
  .contact__dot { width: 8px; height: 8px; border-radius: 50%; background: var(--brand-green); flex: none; }

  .divider {
    position: absolute; left: 60px; right: 60px; top: 342px;
    height: 1px; background: var(--rule-dark);
  }
  .edge-rule {
    position: absolute; left: 0; right: 0; bottom: 44px;
    height: 3px; background: var(--rule-dark);
  }
  .edge-band {
    position: absolute; left: 0; right: 0; bottom: 18px;
    height: 22px; background: var(--band-green);
  }

  .website {
    position: absolute; right: 70px; bottom: 80px;
    font-size: 17px; font-weight: 500; letter-spacing: 4px;
    color: var(--paper-text);
  }
</style>
</head>
<body>
  <section class="card card--front" aria-label="명함 앞면">
    <div class="brand-name">ARC VOLLEY</div>

    <div class="holder">
      <div class="holder__name">박 서 윤</div>
      <div class="holder__title">대표</div>
    </div>

    <div class="contact contact--phone">
      <svg viewBox="0 0 24 24" aria-hidden="true"><path d="M6.6 10.8a15.1 15.1 0 0 0 6.6 6.6l2.2-2.2a1 1 0 0 1 1-.25 11.4 11.4 0 0 0 3.6.57 1 1 0 0 1 1 1V20a1 1 0 0 1-1 1A17 17 0 0 1 3 4a1 1 0 0 1 1-1h3.5a1 1 0 0 1 1 1c0 1.25.2 2.45.57 3.6a1 1 0 0 1-.25 1z"/></svg>
      <span>010-8472-3916</span>
    </div>

    <div class="divider"></div>

    <div class="contact contact--email">
      <span>seoyun.park@arcvolley-example.co.kr</span>
      <svg viewBox="0 0 24 24" aria-hidden="true"><path d="M2 5h20v14H2z" fill="#1f4a2e"/><path d="M2 5l10 8 10-8" fill="none" stroke="#f6f6f4" stroke-width="1.5"/></svg>
    </div>

    <div class="contact contact--address">
      <svg viewBox="0 0 24 24" aria-hidden="true"><path d="M12 2a7 7 0 0 0-7 7c0 5 7 13 7 13s7-8 7-13a7 7 0 0 0-7-7zm0 9.5A2.5 2.5 0 1 1 12 6.5a2.5 2.5 0 0 1 0 5z" fill="#1f4a2e"/></svg>
      <span>경기도 용인시 수지구 풍덕천로 456 미래타워 5층 501호, 502호</span>
    </div>

    <div class="contact contact--instagram">
      <span class="contact__dot"></span>
      <span><span class="contact__label">Instagram</span> arcvolley</span>
    </div>

    <div class="edge-rule"></div>
    <div class="edge-band"></div>
  </section>

  <section class="card card--back" aria-label="명함 뒷면">
    <div class="brand-name">ARC VOLLEY</div>
    <div class="website">WWW.ARCVOLLEY-EXAMPLE.CO.KR</div>
  </section>
</body>
</html>
```